Creative Web design for Tattoo Artist

I am a tattoo artist with a private tattoo/art studio in Spring, TX. I need to design a website for my studio, to include the following "pages" :
-home/about
-FAQ
-Gallery
-Inquiries
-shop
We would like to see designs that are more dark or "moody", and like the colors black/gold.
I'd like my website to reflect my studio, an award winning private, upscale custom only tattoo studio.

I've attached some examples of styles we liked.

Target Market(s)

adults ages 18-50, interested in tattoos, or fine art

Industry/Entity Type

Tattoos/Fine Art/Arts

Coding

Coded - Design and coding required

Number of Pages Required

5+ page

Colors

Designer to choose colors to be used in the design.

Requirements
Must have
• gallery section, and e-commerce page set up so I can begin selling merchandise, I'd like the fonts to flow with my logo design

```html
<!DOCTYPE html>
<html lang="en">
<head>
<meta charset="utf-8">
<title>The Gilded Viper — Tattoo Studio</title>
<link href="https://fonts.googleapis.com/css2?family=Cinzel:wght@400;500;600;700&family=Quicksand:wght@400;500;600;700&display=swap" rel="stylesheet">
<style>
:root{
  --gold:#d6a20e;
  --ink:#0c0c0c;
  --coal:#161616;
  --slate:#1d1d1d;
  --pill:#262626;
  --field:#202020;
  --text:#e9e9e9;
  --muted:#b9b9b9;
  --faint:rgba(0,0,0,.55);
}
*{margin:0;padding:0;box-sizing:border-box}
html,body{width:1200px;height:5217px;overflow:hidden;background:var(--ink)}
body{font-family:"Quicksand",sans-serif;color:var(--text);position:relative}
.section{position:absolute;left:0;width:1200px;overflow:hidden}
.abs{position:absolute}
.serif{font-family:"Cinzel",serif}
.gold{color:var(--gold)}
.btn{position:absolute;background:var(--gold);color:#fff;font-family:"Cinzel",serif;font-weight:600;font-size:11px;letter-spacing:.5px;display:flex;align-items:center;justify-content:center;text-transform:uppercase}
.photo{position:absolute}
.big-num{position:absolute;font-family:"Cinzel",serif;font-weight:700;font-size:150px;line-height:1;color:var(--faint);letter-spacing:-4px}
.sec-title{position:absolute;left:0;width:1200px;text-align:center;font-family:"Cinzel",serif;font-size:30px;font-weight:500;line-height:1}
.rule{position:absolute}
p.copy{font-size:10.5px;line-height:20px;color:var(--muted)}

/* hero */
.hero{top:0;height:624px;background:radial-gradient(ellipse at 45% 35%,#3a3530 0%,#1e1c1a 45%,#0f0f0f 100%)}
.nav a{position:absolute;top:48px;font-size:12px;color:#fff;text-decoration:none;letter-spacing:.3px;font-weight:500}
.nav a.active{color:var(--gold);border-bottom:1px solid var(--gold);padding-bottom:10px}
.brand-mark{position:absolute;left:540px;top:40px;width:120px;text-align:center;font-family:"Cinzel",serif;font-size:13px;line-height:15px;color:#eee;font-weight:500}
.search{position:absolute;left:1000px;top:39px;width:32px;height:32px;border-radius:50%;background:var(--gold)}
.hero h2{position:absolute;top:197px;left:0;width:1200px;text-align:center;font-family:"Cinzel",serif;font-size:27px;font-weight:500;color:#fff}
.hero h1{position:absolute;top:232px;left:0;width:1200px;text-align:center;font-family:"Cinzel",serif;font-size:70px;font-weight:700;line-height:70px;color:var(--gold)}
.hero .lead{position:absolute;top:426px;left:300px;width:600px;text-align:center;font-size:11px;line-height:19px;font-style:italic;color:#ddd}

/* about */
.about{top:624px;height:578px;background:linear-gradient(90deg,#1a1a1a,#121212)}
.about-brand{position:absolute;left:203px;top:26px;width:324px;height:525px;display:flex;align-items:center;justify-content:center;text-align:center;font-family:"Cinzel",serif;font-size:36px;line-height:46px;color:#d9c9c0;font-weight:500}
.about h3{position:absolute;left:624px;top:86px;font-family:"Cinzel",serif;font-size:28px;font-weight:500;line-height:36px}

/* shop */
.shop{top:1202px;height:1478px;background:radial-gradient(ellipse at 50% 40%,#2b2b2b 0%,#1c1c1c 55%,#141414 100%)}
.card-title{position:absolute;text-align:center;font-family:"Cinzel",serif;font-size:17px;font-weight:500;line-height:28px;color:#fff}
.price{position:absolute;text-align:center;font-size:11px;color:var(--gold);font-weight:600}
.card-copy{position:absolute;text-align:center;font-size:10px;line-height:20px;color:var(--muted)}
.frame{position:absolute;border:1.5px solid #cfcfcf}
.frame.goldf{border:8px solid var(--gold);border-left:none;border-bottom:none}
.vert{position:absolute;font-family:"Cinzel",serif;font-size:28px;font-weight:500;color:#ddd;transform:rotate(-90deg);transform-origin:left top;white-space:nowrap}

/* faq */
.faq{top:2680px;height:715px;background:#0b0b0b}
.q{position:absolute;left:253px;width:694px;height:34px;border-radius:17px;background:var(--pill);display:flex;align-items:center}
.q .n{width:32px;height:32px;border-radius:50%;background:#333;margin-left:2px;display:flex;align-items:center;justify-content:center;font-size:10px;font-weight:700}
.q.open .n{background:var(--gold)}
.q .t{margin-left:20px;font-size:10.5px;font-weight:600;letter-spacing:.2px;flex:1}
.q .s{width:40px;text-align:center;color:#777;font-size:16px}
.faq .ans{position:absolute;left:310px;top:395px;width:570px;font-size:10.5px;line-height:21px;color:var(--muted)}

/* gallery */
.gallery{top:3395px;height:983px;background:linear-gradient(180deg,#1f1f1f,#161616)}
.grid{position:absolute;left:162px;top:219px;width:878px;display:flex;gap:8px}
.col{width:213.5px;display:flex;flex-direction:column;gap:8px}
.tile{width:100%}

/* contact */
.contact{top:4378px;height:483px;background:#151515}
.field{position:absolute;background:var(--field);font-size:10px;color:#888;padding:10px 10px}
.info-ic{position:absolute;width:40px;height:40px;border-radius:50%;background:var(--gold);display:flex;align-items:center;justify-content:center}
.info-h{position:absolute;font-size:12px;font-weight:600;color:#fff}
.info-t{position:absolute;font-size:13px;line-height:20px;color:#fff}

/* footer */
.footer{top:4861px;height:356px;background:#0a0a0a}
.f-brand{position:absolute;left:152px;top:50px;width:110px;text-align:center;font-family:"Cinzel",serif;font-size:15px;line-height:22px;color:#ddd}
.f-h{position:absolute;top:46px;font-size:12px;font-weight:700;color:var(--gold)}
.f-list{position:absolute;top:72px;list-style:none;font-size:11px;line-height:21.5px;color:#ddd}
.f-list li::before{content:"»";color:var(--gold);margin-right:12px}
.f-list.social li::before{content:"•"}
.f-ci{position:absolute;width:26px;height:26px;border-radius:50%;background:var(--gold);display:flex;align-items:center;justify-content:center}
.f-ct{position:absolute;font-size:9.5px;line-height:13px;color:#ddd}
.f-in{position:absolute;left:782px;width:256px;border-bottom:1px solid #444;font-size:8px;color:#777;padding-bottom:8px}
</style>
</head>
<body>

<!-- HERO -->
<header class="section hero">
  <div class="photo" role="img" aria-label="Dim close-up of a tattoo machine at work" style="inset:0;background:radial-gradient(ellipse at 50% 20%,rgba(80,70,60,.35),rgba(0,0,0,0) 60%)"></div>
  <nav class="nav">
    <a class="active" style="left:162px">HOME</a>
    <a style="left:245px">ABOUT</a>
    <a style="left:330px">FAQ</a>
    <a style="left:403px">GALLERY</a>
    <a style="left:760px">INQUIRIES</a>
    <a style="left:861px">SHOP</a>
  </nav>
  <div class="brand-mark">The Gilded Viper</div>
  <div class="search"><svg width="32" height="32" viewBox="0 0 32 32"><circle cx="15" cy="15" r="5" fill="none" stroke="#fff" stroke-width="2"/><line x1="19" y1="19" x2="22" y2="22" stroke="#fff" stroke-width="2"/></svg></div>
  <h2>WELCOME TO THE GILDED VIPER</h2>
  <h1>BRING YOUR SKIN BACK<br>TO LIFE</h1>
  <svg class="rule" style="left:283px;top:391px" width="634" height="16"><circle cx="8" cy="8" r="7" fill="#fff"/><polygon points="8,6.5 580,6.5 630,3 600,10 8,9.5" fill="#fff"/></svg>
  <p class="lead">Lorem ipsum dolor sit amet, consectetur adipiscing elit, sed do eiusmod tempor incididunt ut labore et dolore magna aliqua sed do eiusmod tempor.</p>
  <div class="btn" style="left:529px;top:492px;width:142px;height:31px">GET STARTED</div>
  <svg class="abs" style="left:142px;top:537px" width="42" height="16"><line x1="2" y1="8" x2="40" y2="8" stroke="#fff" stroke-width="1.5"/><polyline points="9,2 2,8 9,14" fill="none" stroke="#fff" stroke-width="1.5"/></svg>
  <svg class="abs" style="left:1016px;top:537px" width="42" height="16"><line x1="2" y1="8" x2="40" y2="8" stroke="#fff" stroke-width="1.5"/><polyline points="33,2 40,8 33,14" fill="none" stroke="#fff" stroke-width="1.5"/></svg>
</header>

<!-- ABOUT -->
<section class="section about">
  <div class="about-brand">The<br>Gilded<br>Viper</div>
  <div class="big-num" style="left:620px;top:40px;color:rgba(255,255,255,.05)">01</div>
  <h3>ABOUT THE<br><span class="gold">GILDED VIPER</span></h3>
  <p class="copy abs" style="left:624px;top:196px;width:416px">Lorem ipsum dolor sit amet, consectetur adipiscing elit, sed do eiusmod tempor incididunt ut labore et dolore magna aliqua. Quis ipsum suspendisse ultrices gravida. Risus commodo viverra maecenas accumsan lacus vel facilisis. iste natus error sit voluptatem accusantium doloremque laudantium, totam rem aperiam, iste natus error sit voluptatem accusantium doloremque laudantium, totam rem aperiam, eaque ipsa quae ab illo inventore veritatis et quasi architecto.iste natus error sit voluptatem accusantium doloremque laudantium, totam rem aperiam, eaque ipsa quae ab illo inventore veritatis et quasi architecto beatae vitae dicta sunt explicabo. Nemo enim ipsam voluptatem quia voluptas sit aspernatur aut odit aut fugit, sed quia consequuntur magni dolores eos qui ratione voluptatem sequi nesciunt. Neque porro quisquam est, qui dolorem ipsum quia dolor sit ametexercitationem ullam corporis suscipit laboriosammmod consequatur.</p>
  <div class="btn" style="left:624px;top:450px;width:142px;height:31px">LEARN MORE</div>
</section>

<!-- SHOP -->
<section class="section shop">
  <div class="photo" role="img" aria-label="Faint close-up of a tattoo machine in the background" style="inset:0;background:radial-gradient(circle at 30% 45%,rgba(60,60,60,.35),rgba(0,0,0,0) 40%)"></div>
  <div class="big-num" style="left:496px;top:62px">02</div>
  <div class="sec-title" style="top:133px">SHOP <span class="gold">OUR TATTOO</span></div>
  <svg class="rule" style="left:474px;top:166px" width="250" height="10"><circle cx="5" cy="5" r="4" fill="#fff"/><polygon points="5,4 220,4 248,2 230,6.5 5,6" fill="#fff"/></svg>
  <svg class="abs" style="left:91px;top:391px" width="42" height="16"><line x1="2" y1="8" x2="40" y2="8" stroke="#555" stroke-width="1.5"/><polyline points="9,2 2,8 9,14" fill="none" stroke="#555" stroke-width="1.5"/></svg>
  <svg class="abs" style="left:1068px;top:391px" width="42" height="16"><line x1="2" y1="8" x2="40" y2="8" stroke="#fff" stroke-width="1.5"/><polyline points="33,2 40,8 33,14" fill="none" stroke="#fff" stroke-width="1.5"/></svg>

  <!-- product 1 -->
  <div class="frame" style="left:274px;top:245px;width:279px;height:341px"></div>
  <div class="photo" role="img" aria-label="Woman with a fully tattooed floral sleeve" style="left:239px;top:258px;width:304px;height:340px;background:linear-gradient(135deg,#9c4a4c,#c9b3a8 45%,#6e6a69)"></div>
  <div class="vert" style="left:187px;top:598px">LOREM IPSUM</div>
  <div class="card-title" style="left:592px;top:294px;width:416px">LOREM IPSUM DOLOR SIT AMET<br>CONSECTETUR ADIPISCING ELIT, SED DO</div>
  <div class="price" style="left:592px;top:356px;width:416px">$ 120.00</div>
  <div class="card-copy" style="left:592px;top:375px;width:416px">Lorem ipsum dolor sit amet, consectetur adipiscing elit, sed do eiusmod tempor incididunt ut labore et dolore magna aliqua. Quis ipsum suspendisse ultrices gravida. Risus commodo viverra maecenas accumsan lacus vel facilisis. iste natus error sit voluptatem accusantium doloremque laudantium, totam rem aperiam, iste natus error sit voluptatem accusantium doloremque laudantium, totam rem aperiam, eaque ipsa quae ab illo inventore veritatis et quasi architecto.iste natus error sit voluptatem accusantium doloremque laudantium totam rem aperiam.</div>
  <div class="btn" style="left:730px;top:525px;width:142px;height:32px">LEARN MORE</div>

  <!-- product 2 -->
  <div class="card-title" style="left:193px;top:695px;width:416px">LOREM IPSUM DOLOR SIT AMET<br>CONSECTETUR ADIPISCING ELIT, SED DO</div>
  <div class="price" style="left:193px;top:757px;width:416px">$ 120.00</div>
  <div class="card-copy" style="left:193px;top:776px;width:416px">Lorem ipsum dolor sit amet, consectetur adipiscing elit, sed do eiusmod tempor incididunt ut labore et dolore magna aliqua. Quis ipsum suspendisse ultrices gravida. Risus commodo viverra maecenas accumsan lacus vel facilisis. iste natus error sit voluptatem accusantium doloremque laudantium, totam rem aperiam, iste natus error sit voluptatem accusantium doloremque laudantium, totam rem aperiam, eaque ipsa quae ab illo inventore veritatis et quasi architecto.iste natus error sit voluptatem accusantium doloremque laudantium totam rem aperiam.</div>
  <div class="btn" style="left:328px;top:926px;width:142px;height:32px">LEARN MORE</div>
  <div class="frame goldf" style="left:683px;top:649px;width:278px;height:338px"></div>
  <div class="photo" role="img" aria-label="Man with a heavily tattooed chest and arms" style="left:645px;top:663px;width:304px;height:338px;background:linear-gradient(160deg,#3c4048,#5d5650 50%,#2a2c30)"></div>
  <div class="vert" style="left:975px;top:1001px">LOREM IPSUM</div>

  <!-- product 3 -->
  <div class="frame" style="left:274px;top:1052px;width:279px;height:308px"></div>
  <div class="photo" role="img" aria-label="Woman seen from behind with a large back tattoo" style="left:239px;top:1064px;width:304px;height:339px;background:linear-gradient(180deg,#1a2430,#46403f 55%,#1b2028)"></div>
  <div class="vert" style="left:187px;top:1403px">LOREM IPSUM</div>
  <div class="card-title" style="left:592px;top:1099px;width:416px">LOREM IPSUM DOLOR SIT AMET<br>CONSECTETUR ADIPISCING ELIT, SED DO</div>
  <div class="price" style="left:592px;top:1160px;width:416px">$ 120.00</div>
  <div class="card-copy" style="left:592px;top:1179px;width:416px">Lorem ipsum dolor sit amet, consectetur adipiscing elit, sed do eiusmod tempor incididunt ut labore et dolore magna aliqua. Quis ipsum suspendisse ultrices gravida. Risus commodo viverra maecenas accumsan lacus vel facilisis. iste natus error sit voluptatem accusantium doloremque laudantium, totam rem aperiam, iste natus error sit voluptatem accusantium doloremque laudantium, totam rem aperiam, eaque ipsa quae ab illo inventore veritatis et quasi architecto.iste natus error sit voluptatem accusantium doloremque laudantium totam rem aperiam.</div>
  <div class="btn" style="left:730px;top:1331px;width:142px;height:32px">LEARN MORE</div>
</section>

<!-- FAQ -->
<section class="section faq">
  <div class="big-num" style="left:492px;top:54px;color:rgba(255,255,255,.05)">03</div>
  <div class="sec-title" style="top:123px">FREQUENTLY <span class="gold">ASKED QUESTIONS</span></div>
  <svg class="rule" style="left:474px;top:157px" width="250" height="10"><circle cx="5" cy="5" r="4" fill="#fff"/><polygon points="5,4 220,4 248,2 230,6.5 5,6" fill="#fff"/></svg>
  <div class="q" style="top:218px"><span class="n">01</span><span class="t">LOREM IPSUM DOLOR SIT AMET, CONSECTETUR ADIPISCING ELIT SED DO EIUSMOD ?</span><span class="s">+</span></div>
  <div class="q" style="top:277px"><span class="n">02</span><span class="t">LOREM IPSUM DOLOR SIT AMET, CONSECTETUR ADIPISCING ELIT SED DO EIUSMOD ?</span><span class="s">+</span></div>
  <div class="q open" style="top:335px"><span class="n">03</span><span class="t">LOREM IPSUM DOLOR SIT AMET, CONSECTETUR ADIPISCING ELIT SED DO EIUSMOD ?</span><span class="s" style="color:var(--gold)">-</span></div>
  <p class="ans">Lorem ipsum dolor sit amet, consectetur adipiscing elit, sed do eiusmod tempor incididunt ut labore et dolore magna aliqua. Ut enim ad minim veniam, quis nostrud exercitation ullamco laboris nisi ut aliquip ex ea commodo consequat. Duis aute irure dolor in reprehenderit in voluptate velit esse cillum dolore eu fugiat nulla pariatur. Excepteur sint occaecat cupidatat non proident, sunt in culpa qui officia deserunt mollit anim id est laborum.</p>
  <div class="q" style="top:500px"><span class="n">04</span><span class="t">LOREM IPSUM DOLOR SIT AMET, CONSECTETUR ADIPISCING ELIT SED DO EIUSMOD ?</span><span class="s">+</span></div>
  <div class="q" style="top:558px"><span class="n">05</span><span class="t">LOREM IPSUM DOLOR SIT AMET, CONSECTETUR ADIPISCING ELIT SED DO EIUSMOD ?</span><span class="s">+</span></div>
  <div class="q" style="top:617px"><span class="n">06</span><span class="t">LOREM IPSUM DOLOR SIT AMET, CONSECTETUR ADIPISCING ELIT SED DO EIUSMOD ?</span><span class="s">+</span></div>
</section>

<!-- GALLERY -->
<section class="section gallery">
  <div class="big-num" style="left:492px;top:50px">04</div>
  <div class="sec-title" style="top:119px">OUR <span class="gold">TATTOO GALLERY</span></div>
  <svg class="rule" style="left:474px;top:151px" width="250" height="10"><circle cx="5" cy="5" r="4" fill="#fff"/><polygon points="5,4 220,4 248,2 230,6.5 5,6" fill="#fff"/></svg>
  <div class="grid">
    <div class="col">
      <div class="tile" role="img" aria-label="Artist tattooing an arm" style="height:201px;background:linear-gradient(135deg,#3a2a22,#a4785e)"></div>
      <div class="tile" role="img" aria-label="Tattoo artist at work in the studio" style="height:202px;background:linear-gradient(135deg,#2a3030,#5f6a62)"></div>
      <div class="tile" role="img" aria-label="Gloved hands inking a mandala design" style="height:270px;background:linear-gradient(160deg,#2b2b2b,#8a8480)"></div>
    </div>
    <div class="col">
      <div class="tile" role="img" aria-label="Close-up of fresh ink on skin" style="height:274px;background:linear-gradient(160deg,#262626,#7a5442)"></div>
      <div class="tile" role="img" aria-label="Woman with arm tattoos outdoors" style="height:196px;background:linear-gradient(180deg,#4f4b49,#2e2e2e)"></div>
      <div class="tile" role="img" aria-label="Tattoo session under a studio lamp" style="height:195px;background:linear-gradient(135deg,#4e4e4e,#bdbdbd)"></div>
    </div>
    <div class="col">
      <div class="tile" role="img" aria-label="Tattoo machine held in gloved hands" style="height:201px;background:linear-gradient(135deg,#1e1e1e,#7b7b7b)"></div>
      <div class="tile" role="img" aria-label="Artist tattooing under blue light" style="height:202px;background:linear-gradient(135deg,#0f1a30,#3b4f7a)"></div>
      <div class="tile" role="img" aria-label="Woman with purple hair and tattooed arms" style="height:270px;background:linear-gradient(135deg,#5a2e6e,#b9a5bb)"></div>
    </div>
    <div class="col">
      <div class="tile" role="img" aria-label="Tattooed man adjusting a bow tie" style="height:274px;background:linear-gradient(180deg,#2c2c2c,#6e5a48)"></div>
      <div class="tile" role="img" aria-label="Tattooed hands and forearms" style="height:196px;background:linear-gradient(135deg,#38424e,#6b5d58)"></div>
      <div class="tile" role="img" aria-label="Fresh tattoo being wrapped" style="height:195px;background:linear-gradient(135deg,#4a3526,#b48a6a)"></div>
    </div>
  </div>
</section>

<!-- CONTACT -->
<section class="section contact">
  <div class="big-num" style="left:496px;top:40px;color:rgba(0,0,0,.45)">05</div>
  <div class="sec-title" style="top:102px">GET <span class="gold">IN TOUCH</span></div>
  <svg class="rule" style="left:490px;top:135px" width="230" height="10"><circle cx="5" cy="5" r="4" fill="#fff"/><polygon points="5,4 200,4 228,2 210,6.5 5,6" fill="#fff"/></svg>
  <div class="field" style="left:184px;top:207px;width:257px;height:34px">First name</div>
  <div class="field" style="left:450px;top:207px;width:257px;height:34px">Last name</div>
  <div class="field" style="left:184px;top:256px;width:257px;height:34px">Email Address</div>
  <div class="field" style="left:450px;top:256px;width:257px;height:34px">Phone Number</div>
  <div class="field" style="left:184px;top:304px;width:257px;height:34px">What Tattoo ?</div>
  <div class="field" style="left:450px;top:304px;width:257px;height:86px">Message</div>
  <div class="btn" style="left:184px;top:355px;width:257px;height:35px">SUBMIT NOW</div>

  <div class="info-ic" style="left:744px;top:203px"><svg width="16" height="20" viewBox="0 0 16 20"><path d="M8 1a6 6 0 0 0-6 6c0 5 6 12 6 12s6-7 6-12a6 6 0 0 0-6-6z" fill="#fff"/><circle cx="8" cy="7" r="2.3" fill="var(--gold)"/></svg></div>
  <div class="info-h" style="left:797px;top:200px">Location</div>
  <div class="info-t" style="left:797px;top:218px;width:250px">123 Lorem ipsum dolor sit amet cons ectetur adipiscing elit.</div>
  <div class="info-ic" style="left:744px;top:280px"><svg width="18" height="18" viewBox="0 0 18 18"><path d="M4 2l3 3-2 2c1 2 3 4 5 5l2-2 3 3-2 3C8 16 2 10 1 4z" fill="#fff"/></svg></div>
  <div class="info-h" style="left:797px;top:279px">Phone Number</div>
  <div class="info-t" style="left:797px;top:297px">+1 123 456 7890</div>
  <div class="info-ic" style="left:744px;top:351px"><svg width="18" height="14" viewBox="0 0 18 14"><rect x="1" y="1" width="16" height="12" fill="#fff"/><polyline points="1,1 9,8 17,1" fill="none" stroke="var(--gold)" stroke-width="1.5"/></svg></div>
  <div class="info-h" style="left:797px;top:350px">Email Address</div>
  <div class="info-t" style="left:797px;top:368px">info@gildedviper.com</div>
</section>

<!-- FOOTER -->
<footer class="section footer">
  <div class="f-brand">The<br>Gilded<br>Viper</div>
  <div class="f-h" style="left:288px">Quick Links</div>
  <ul class="f-list" style="left:288px"><li>Home</li><li>About</li><li>FAQ</li><li>Gallery</li><li>Inquiries</li><li>Shop</li></ul>
  <div class="f-h" style="left:424px">Follow Us</div>
  <ul class="f-list social" style="left:424px"><li>Friendbook</li><li>Snapgram</li><li>Pinboard</li><li>Clipstream</li><li>Worknet</li></ul>
  <div class="f-h" style="left:559px">Contact Info</div>
  <div class="f-ci" style="left:560px;top:78px"><svg width="10" height="13" viewBox="0 0 16 20"><path d="M8 1a6 6 0 0 0-6 6c0 5 6 12 6 12s6-7 6-12a6 6 0 0 0-6-6z" fill="#fff"/></svg></div>
  <div class="f-ct" style="left:599px;top:74px;width:130px">Location<br>123 Lorem ipsum dolor sit ectetur adipiscing elit.</div>
  <div class="f-ci" style="left:560px;top:133px"><svg width="12" height="12" viewBox="0 0 18 18"><path d="M4 2l3 3-2 2c1 2 3 4 5 5l2-2 3 3-2 3C8 16 2 10 1 4z" fill="#fff"/></svg></div>
  <div class="f-ct" style="left:599px;top:131px">Phone Number<br>+1 123 456 7890</div>
  <div class="f-ci" style="left:560px;top:194px"><svg width="12" height="10" viewBox="0 0 18 14"><rect x="1" y="1" width="16" height="12" fill="#fff"/></svg></div>
  <div class="f-ct" style="left:599px;top:192px">Email Address<br>info@gildedviper.com</div>
  <div class="f-h" style="left:782px">Our Newsletter</div>
  <div class="f-ct" style="left:782px;top:72px;width:265px">Lorem ipsum dolor sit amet, consectetur adipiscing elitsed do eiusmod tempor incididunt ut</div>
  <div class="f-in" style="top:130px">Enter The Name*</div>
  <div class="f-in" style="top:178px">Enter The Email*</div>
  <div class="btn" style="left:782px;top:223px;width:144px;height:32px">SUBSCRIBE NOW</div>
  <div class="abs" style="left:152px;top:289px;width:896px;height:1px;background:#3a3a3a"></div>
  <div class="abs" style="left:0;top:315px;width:1200px;text-align:center;font-size:10px;color:#ddd">© copyrights 2023 <span class="gold" style="font-weight:600">The Gilded Viper</span> &nbsp;|&nbsp;&nbsp; All rights reserved.</div>
</footer>

</body>
</html>
```